Flayer design for American style Pizza Company

We need to enhance an A5 flayer which we didn’t print yet because it doesn’t look good. We will send the file to the designer (PSD format) and we need a design that look like a fast food companies (RJD, Sizzle dock, Mollers ,,etc.). Also some products picture which are included in the file needs to be improved (brightness , contrast, size, etc.). We may also provied the origenal master photos for the products.

please download the main files from http://qx.fm/tarquelOdu

Please dowload Products Pictures from http://qx.fm/m4pLsWeT7c

please download the main files from     http://qx.fm/tarquelOdu                     

hi all

Best Regards       

                                   

                                        Please dowload Products Pictures from     http://qx.fm/m4pLsWeT7c     

                                   

Reason: Hi all I guarantee to accept the design which sticks with the requirements. The submitted design will be compared before approval with ,Sizzle Dock, RJD, Fiora Lane etc designs. GoodLuck all Best Regards

It Company

```html
<!DOCTYPE html>
<html lang="ar">
<head>
<meta charset="utf-8">
<title>Crusto Oven – Tortilla Flyer</title>
<link href="https://fonts.googleapis.com/css2?family=Cairo:wght@600;700;800;900&family=Roboto:wght@700;900&display=swap" rel="stylesheet">
<style>
  :root {
    --stage: #e4e4e2;
    --red: #e31b23;
    --red-deep: #c20f16;
    --red-shadow: #a80d12;
    --orange: #f58a1f;
    --yellow: #fcc42a;
    --green: #3fa54a;
    --green-deep: #2b8a37;
    --gold: #f3b233;
    --white: #ffffff;
    --photo-warm: #d9a15b;
    --photo-dark: #6b3a1c;
  }
  * { box-sizing: border-box; margin: 0; padding: 0; }
  html, body { width: 1200px; height: 800px; overflow: hidden; }
  body {
    background: var(--stage);
    font-family: "Cairo", sans-serif;
    position: relative;
  }
  .flyer {
    position: absolute;
    top: 18px;
    width: 538px;
    height: 762px;
    overflow: hidden;
    background: radial-gradient(ellipse at 50% 40%, var(--yellow) 0%, var(--orange) 35%, var(--red) 75%);
    box-shadow: 0 4px 14px rgba(0,0,0,.25);
  }
  .flyer--front { left: 32px; }
  .flyer--menu  { left: 631px; background: radial-gradient(ellipse at 50% 45%, var(--yellow) 0%, var(--orange) 30%, var(--red) 70%); }

  /* front */
  .hero-photo {
    position: absolute; left: 0; top: 170px; width: 538px; height: 320px;
    background: radial-gradient(ellipse at 50% 60%, var(--photo-warm) 0%, #b8723a 45%, var(--photo-dark) 85%, rgba(107,58,28,0) 100%);
    opacity: .9;
  }
  .headline-ribbon { position: absolute; left: 0; top: 50px; width: 538px; height: 150px; }
  .headline-ribbon svg { width: 100%; height: 100%; display: block; overflow: visible; }
  .headline-text {
    fill: var(--white);
    font-family: "Cairo", sans-serif;
    font-weight: 900; font-size: 34px;
  }
  .new-badge {
    position: absolute; left: 336px; top: 160px; width: 130px; height: 130px;
  }
  .new-badge span {
    position: absolute; inset: 0; display: flex; align-items: center; justify-content: center;
    color: var(--white); font-weight: 900; font-size: 44px; transform: rotate(-8deg);
  }
  .halal-mark {
    position: absolute; left: 28px; top: 292px; width: 36px; height: 36px;
    border-radius: 50%; border: 2px solid var(--white);
  }
  .green-band {
    position: absolute; left: 0; right: 0; top: 486px; bottom: 0;
    background: linear-gradient(90deg, var(--red) 0%, var(--red) 42%, #f1ece4 52%, var(--green) 62%, var(--green-deep) 100%);
  }
  .green-band::before {
    content: ""; position: absolute; left: 0; right: 0; top: 0; height: 110px;
    background: linear-gradient(90deg, var(--green) 0%, var(--green-deep) 100%);
  }
  .tagline-oval {
    position: absolute; left: 24px; top: 458px; width: 492px; height: 160px;
    border-radius: 50%;
    background: var(--red);
    border: 3px solid var(--gold);
    display: flex; align-items: center; justify-content: center; text-align: center;
    color: var(--white); font-weight: 800; font-size: 42px; line-height: 1.2;
  }
  .front-footer { position: absolute; left: 0; right: 0; top: 618px; bottom: 0; }
  .delivery-en {
    position: absolute; left: 46px; width: 236px; top: 10px; text-align: right; color: var(--white);
    font-family: "Roboto", sans-serif; font-weight: 700; font-size: 20px;
  }
  .delivery-ar {
    position: absolute; left: 46px; width: 236px; top: 34px; text-align: right; color: var(--white);
    font-weight: 800; font-size: 22px; line-height: 1.3;
  }
  .phone {
    position: absolute; color: var(--white);
    font-family: "Roboto", sans-serif; font-weight: 900; letter-spacing: 1px;
    white-space: nowrap;
  }
  .front-footer .phone { left: 20px; top: 82px; font-size: 46px; }
  .brand {
    position: absolute; display: flex; align-items: center; gap: 6px;
    background: var(--white); border-radius: 50%; padding: 8px 20px;
    color: var(--red); font-weight: 800; font-size: 20px; white-space: nowrap;
  }
  .brand::before {
    content: ""; width: 16px; height: 16px; border-radius: 50%; background: var(--red);
  }
  .front-footer .brand { left: 336px; top: 66px; }

  /* menu */
  .menu-grid {
    position: absolute; left: 20px; top: 22px;
    display: grid; grid-template-columns: 232px 232px; column-gap: 32px; row-gap: 24px;
  }
  .menu-card {
    position: relative; width: 232px; height: 186px;
    background: var(--white); border-radius: 8px;
    border: 2px solid var(--red-deep);
  }
  .menu-card__label {
    position: absolute; left: 6px; right: 6px; top: 14px; height: 40px;
    background: var(--red); border-radius: 4px;
    color: var(--white); font-weight: 800; font-size: 22px; line-height: 40px; text-align: center;
    box-shadow: 0 2px 0 var(--red-deep);
  }
  .menu-card__photo {
    position: absolute; left: 10px; right: 10px; top: 62px; bottom: 12px;
    border-radius: 6px;
    background: radial-gradient(ellipse at 50% 65%, #e7c08a 0%, #f3e4cc 55%, var(--white) 85%);
  }
  .menu-footer {
    position: absolute; left: 0; right: 0; top: 648px; height: 100px;
    background: linear-gradient(90deg, var(--red) 0%, var(--red) 50%, #f1ece4 58%, var(--green) 68%, var(--green-deep) 100%);
  }
  .menu-footer .delivery-line {
    position: absolute; left: 20px; top: 8px; color: var(--white);
    font-family: "Roboto", sans-serif; font-weight: 700; font-size: 14px;
    display: flex; gap: 10px; align-items: center;
  }
  .menu-footer .delivery-line span:last-child { font-family: "Cairo", sans-serif; font-weight: 800; font-size: 15px; }
  .menu-footer .phone { left: 20px; top: 32px; font-size: 46px; }
  .menu-footer .brand { left: 334px; top: 30px; }
</style>
</head>
<body>

<article class="flyer flyer--front">
  <div class="hero-photo" role="img" aria-label="Grilled tortilla rolls on a wooden board with tomato, falafel and olives"></div>

  <div class="headline-ribbon">
    <svg viewBox="0 0 538 150">
      <defs>
        <path id="headline-curve" d="M58 118 Q270 62 484 52"/>
      </defs>
      <!-- folded tails -->
      <path d="M62 96 L10 110 L30 128 L12 148 L66 138 Z" fill="var(--red-deep)" stroke="var(--gold)" stroke-width="3"/>
      <path d="M478 30 L530 22 L514 42 L532 64 L480 72 Z" fill="var(--red-deep)" stroke="var(--gold)" stroke-width="3"/>
      <path d="M62 96 L50 86 L50 126 L66 138 Z" fill="var(--red-shadow)"/>
      <path d="M478 30 L490 20 L492 62 L480 72 Z" fill="var(--red-shadow)"/>
      <!-- curved band -->
      <path d="M48 86 Q270 28 492 20 L492 74 Q270 82 48 140 Z" fill="var(--red)" stroke="var(--gold)" stroke-width="4" stroke-linejoin="round"/>
      <text class="headline-text" direction="rtl">
        <textPath href="#headline-curve" startOffset="50%" text-anchor="middle">ابدأ يومك بفطائر التورتيلا</textPath>
      </text>
    </svg>
  </div>

  <div class="new-badge">
    <svg viewBox="0 0 130 130" aria-hidden="true">
      <polygon fill="var(--white)" points="65,2 75,17 91,8 95,26 113,23 111,41 128,46 118,61 128,76 112,82 115,100 97,99 92,117 76,109 65,124 54,109 38,117 33,99 15,100 18,82 2,76 12,61 2,46 19,41 17,23 35,26 39,8 55,17"/>
      <circle cx="65" cy="63" r="48" fill="var(--green)"/>
    </svg>
    <span>جديد</span>
  </div>

  <div class="halal-mark" aria-hidden="true"></div>

  <div class="green-band"></div>
  <p class="tagline-oval">تورتيلا محمصة تصلك<br>ساخنة وهشة</p>

  <footer class="front-footer">
    <p class="delivery-en">Fast delivery service</p>
    <p class="delivery-ar">خدمة توصيل سريعة</p>
    <p class="phone">037 555 918</p>
    <p class="brand">أفران كرستو</p>
  </footer>
</article>

<article class="flyer flyer--menu">
  <div class="menu-grid" dir="rtl">
    <section class="menu-card">
      <h2 class="menu-card__label">تورتيلا الدجاج</h2>
      <div class="menu-card__photo" role="img" aria-label="Chicken tortilla rolls with cheese and lettuce"></div>
    </section>
    <section class="menu-card">
      <h2 class="menu-card__label">تورتيلا الفلافل</h2>
      <div class="menu-card__photo" role="img" aria-label="Falafel tortilla rolls with tomato and herbs"></div>
    </section>
    <section class="menu-card">
      <h2 class="menu-card__label">تورتيلا الفيتا</h2>
      <div class="menu-card__photo" role="img" aria-label="Feta tortilla rolls with tomato and za'atar"></div>
    </section>
    <section class="menu-card">
      <h2 class="menu-card__label">تورتيلا التونا</h2>
      <div class="menu-card__photo" role="img" aria-label="Tuna tortilla rolls with pepper, onion and olives"></div>
    </section>
    <section class="menu-card">
      <h2 class="menu-card__label">تورتيلا الجبنة</h2>
      <div class="menu-card__photo" role="img" aria-label="Cheese tortilla rolls with cucumber, tomato and olives"></div>
    </section>
    <section class="menu-card">
      <h2 class="menu-card__label">تورتيلا لبنة زعتر</h2>
      <div class="menu-card__photo" role="img" aria-label="Labneh and za'atar tortilla rolls with a bowl of labneh"></div>
    </section>
  </div>

  <footer class="menu-footer">
    <p class="delivery-line"><span>Fast delivery service</span><span>خدمة توصيل سريعة</span></p>
    <p class="phone">037 555 918</p>
    <p class="brand">أفران كرستو</p>
  </footer>
</article>

</body>
</html>
```